Startup Technology Consulting Firm in NYC Needs A Website

I need a website built for my startup technology consulting company Larkspur Systems Group. We offer a unique white glove service that provides end to end technology support. I want to stand out above the rest. We are small firm but are very dedicated which where we derive our name from LSG primarily offers
end to end technology advisory services to small businesses lacking their own IT staff. We offer top notch white glove and our customer service and satisfaction is exceed by no one.

Below are some of what we provide our clients

Strategic IT Planning
Business Continuity Planning/Disaster Recovery
Cloud Computing\DataCenter Solutions
Server Infrastructure/Networking
Virtualization Technologies
Project Management

Our Technology Advisors hold many certifications from Quorvane & Zelpix. We are also Quorvane Partners

I have attached my logo (preview design) As soon as I ge the final images I will upload.

Industry/Entity Type

Information Technology

Coding

Coded - Design and coding required

Number of Pages Required

1 page

Font styles to use
Sans Serif

Requirements
Must have
• Attract Target Market. The site should bleed the company vision
• DEDICATION everything about the site should show this
• Layout the Benefits of our offerings
• Links to my social media
• Links to dircct my client's for remote support

```html
<!DOCTYPE html>
<html lang="en">
<head>
<meta charset="utf-8">
<title>Larkspur Systems Group</title>
<link href="https://fonts.googleapis.com/css2?family=Open+Sans:wght@400;600;700&family=Play:wght@400;700&display=swap" rel="stylesheet">
<style>
:root{
  --red:#e0262b;
  --blue:#3a5ba8;
  --navy:#1f3f7a;
  --orange:#f28c12;
  --green:#8cc63f;
  --teal:#117f8f;
  --ink:#3c3c3c;
  --text:#555;
  --light:#f3f3f4;
  --dark:#1d2022;
  --white:#fff;
}
*{margin:0;padding:0;box-sizing:border-box}
html,body{width:1200px;height:3077px;overflow:hidden;background:var(--white)}
body{font-family:"Open Sans",Arial,sans-serif;color:var(--text);font-size:14px;line-height:1.38;position:relative}
.abs{position:absolute}
h2,h3,.display{font-family:"Play",Arial,sans-serif;font-weight:700}
p{font-size:14px}
.btn{position:absolute;display:inline-flex;align-items:center;gap:8px;height:30px;padding:0 14px;font-size:12px;text-decoration:none;border-radius:2px}
.btn svg{width:14px;height:8px}
.btn-outline-red{border:1px solid var(--red);color:var(--red)}
.btn-outline-blue{border:1px solid var(--blue);color:var(--blue)}
.btn-dark{background:#333;color:#fff}
.btn-ghost{border:1px solid #ccc;color:#fff}
.btn-red{background:var(--red);color:#fff}

/* header */
.site-header{top:0;left:0;width:1200px;height:58px;background:#fff}
.phone{left:188px;top:20px;font-size:12px;color:var(--navy);display:flex;align-items:center;gap:8px}
.brand-box{left:510px;top:0;width:180px;height:96px;background:#fff;z-index:3;display:flex;flex-direction:column;align-items:center;justify-content:center;gap:6px;box-shadow:0 2px 6px rgba(0,0,0,.15)}
.brand-mark{width:40px;height:40px;border-radius:50%;background:#9fb3c9}
.brand-name{font-size:13px;font-weight:600;color:var(--navy);text-align:center;line-height:1.1}
.menu-toggle{left:988px;top:22px}

/* hero */
.hero{top:58px;left:0;width:1200px;height:524px;background:linear-gradient(120deg,#596777,#c9cfd4 45%,#8a8f94 70%,#6a89b8)}
.hero-title{left:430px;top:172px;width:340px;padding:8px 0;background:rgba(20,20,20,.45);text-align:center;color:#fff}
.hero-title .big{font-family:"Play",sans-serif;font-size:40px;letter-spacing:2px;line-height:1}
.hero-title .small{font-family:"Play",sans-serif;font-size:17px;letter-spacing:2px}
.play{left:566px;top:272px;width:68px;height:68px;border-radius:50%;background:rgba(20,20,20,.65);display:flex;align-items:center;justify-content:center}

/* strategic */
.strategic{top:582px;left:0;width:1200px;height:653px;background:#fff}
.strategic h2{position:absolute;top:68px;width:1200px;text-align:center;font-size:27px;color:var(--red)}
.strategic h3{left:188px;top:125px;font-size:15px;color:var(--red);font-family:"Open Sans",sans-serif}
.strategic .col-a{left:188px;top:150px;width:420px}
.strategic .col-b{left:640px;top:152px;width:360px}
.strategic .btn{left:188px;top:284px}
.desk-photo{left:0;top:220px;width:1200px;height:433px;background:linear-gradient(180deg,rgba(255,255,255,0) 0,#e6e8ea 30%,#3b4a66 62%,#16b6c7 88%,#2a3550)}

/* continuity */
.continuity{top:1235px;left:0;width:1200px;height:477px;background:var(--light)}
.continuity .kicker{left:188px;top:68px;font-size:27px;color:var(--blue);line-height:1}
.continuity .headline{left:186px;top:100px;font-size:60px;color:var(--blue);line-height:1}
.continuity .rule{left:188px;top:170px;width:312px;height:1px;background:#bbb}
.continuity .sub{left:188px;top:175px;font-size:31px;color:var(--ink);font-weight:400}
.continuity h3{left:600px;top:70px;font-size:17px;color:var(--blue)}
.continuity .body{left:600px;top:104px;width:420px}
.continuity .body p{margin-bottom:14px}
.continuity a.inline{color:var(--blue);text-decoration:none}
.continuity .btn{left:600px;top:375px}

/* cloud */
.cloud{top:1712px;left:0;width:1200px;height:468px;background:#fff}
.cloud h3{font-size:19px;color:#222}
.cloud .c1{left:188px;top:82px;width:370px}
.cloud .c2{left:665px;top:82px;width:360px}
.cloud h3+p{margin-top:6px}
.cloud .btn{margin-top:14px;position:relative}
.city{left:160px;top:170px;width:880px;height:278px;background:linear-gradient(180deg,rgba(255,255,255,0),#bfe0e5 40%,#4d98a6 80%,#1d5f6d)}
.city-band{left:0;top:448px;width:1200px;height:20px;background:var(--teal)}

/* server */
.server{top:2180px;left:0;width:1200px;height:278px;background:linear-gradient(90deg,#111 0,#2c3033 20%,#1a1c1e 50%,#2c3033 80%,#111)}
.server h2{position:absolute;top:76px;width:1200px;text-align:center;font-size:22px;color:#fff}
.server h2 span{color:var(--green)}
.server p{position:absolute;top:108px;left:320px;width:560px;text-align:center;color:#fff}
.server .btn{left:548px;top:172px}

/* project */
.project{top:2458px;left:0;width:1200px;height:502px;background:#fff}
.team-photo{left:560px;top:0;width:640px;height:502px;background:linear-gradient(90deg,#fff 0,#e9ecef 18%,#c7a98a 55%,#2f4268 80%,#6d7c8e)}
.project h2{left:188px;top:94px;font-size:25px;color:var(--orange)}
.project .intro{left:188px;top:134px;width:390px}
.project h3{left:188px;top:232px;font-size:16px;color:var(--ink);font-family:"Open Sans",sans-serif}
.project ul{list-style:none}
.project li{font-size:14px;line-height:18.5px}
.project li::before{content:"•";margin:0 10px 0 0}
.project .list-a{left:188px;top:260px}
.project .list-b{left:388px;top:258px}
.project .btn{left:188px;top:374px}
.remote{left:1012px;top:2935px;height:34px;z-index:4;box-shadow:0 2px 4px rgba(0,0,0,.25)}

/* footer */
.site-footer{top:2960px;left:0;width:1200px;height:117px;background:#fff;border-top:1px solid #eee}
.copyright{left:188px;top:62px;font-size:10px;color:#555}
.footer-brand{left:500px;top:30px;width:200px;display:flex;flex-direction:column;align-items:center;gap:4px}
.footer-brand .brand-mark{width:30px;height:30px}
.social{left:906px;top:54px;display:flex;gap:4px}
.social a{width:18px;height:18px;display:block;border-radius:2px}
</style>
</head>
<body>

<header class="site-header abs">
  <div class="phone abs">
    <svg width="12" height="12" viewBox="0 0 24 24"><path fill="#1f3f7a" d="M6.6 10.8a15 15 0 0 0 6.6 6.6l2.2-2.2c.3-.3.7-.4 1-.2 1.1.4 2.3.6 3.6.6.6 0 1 .4 1 1V20c0 .6-.4 1-1 1A17 17 0 0 1 3 4c0-.6.4-1 1-1h3.5c.6 0 1 .4 1 1 0 1.3.2 2.5.6 3.6.1.3 0 .7-.2 1z"/></svg>
    212-555-0148
  </div>
  <div class="brand-box abs">
    <span class="brand-mark"></span>
    <span class="brand-name">Larkspur Systems Group</span>
  </div>
  <svg class="menu-toggle abs" width="26" height="16" viewBox="0 0 26 16"><rect width="26" height="3" fill="#1f3f7a"/><rect y="6.5" width="26" height="3" fill="#1f3f7a"/><rect y="13" width="26" height="3" fill="#1f3f7a"/></svg>
</header>

<section class="hero abs" role="img" aria-label="Photo of a business team meeting around a conference table">
  <div class="hero-title abs">
    <div class="big">LARKSPUR</div>
    <div class="small">SYSTEMS GROUP</div>
  </div>
  <div class="play abs">
    <svg width="26" height="30" viewBox="0 0 26 30"><path d="M2 1l23 14L2 29z" fill="#fff"/></svg>
  </div>
</section>

<section class="strategic abs">
  <div class="desk-photo abs" role="img" aria-label="Overhead photo of colleagues working with laptops and phones at a desk"></div>
  <h2>STRATEGIC IT PLANNING</h2>
  <h3 class="abs">Lorem Ipsum available</h3>
  <p class="col-a abs">There are many variations of passages of Lorem Ipsum available, but the majority have suffered alteration in some form, by injected humour, or randomised words which don't look even slightly believable. If you are going to use a passage of Lorem Ipsum, you need to be sure there isn't anything embarrassing hidden in the middle of text.</p>
  <p class="col-b abs">There are many variations of passages of Lorem Ipsum available, but the majority have suffered.</p>
  <a class="btn btn-outline-red" href="#">Read More <svg viewBox="0 0 14 8"><path d="M0 4h12M9 1l3 3-3 3" stroke="currentColor" fill="none"/></svg></a>
</section>

<section class="continuity abs">
  <div class="kicker display abs">BUSINESS CONTINUITY</div>
  <div class="headline display abs">PLANNING</div>
  <div class="rule abs"></div>
  <div class="sub display abs">Disaster Recovery</div>
  <h3 class="abs">Lorem Ipsum available</h3>
  <div class="body abs">
    <p>There are many variations of passages of <a class="inline" href="#">Lorem Ipsum available</a>, but the majority have suffered alteration in some form, by injected humour, or randomised words which don't look even slightly believable. If you are going to use a passage of <a class="inline" href="#">Lorem Ipsum</a>, you need to be sure there isn't anything embarrassing hidden in the middle of text.</p>
    <p>There are many variations of passages of <a class="inline" href="#">Lorem Ipsum available</a>, but the majority have suffered alteration in some form, by injected humour, or <a class="inline" href="#">randomised words</a> which don't look even slightly believable.</p>
    <p>There are <a class="inline" href="#">many variations</a> of passages of Lorem Ipsum available, but the majority have suffered.</p>
  </div>
  <a class="btn btn-outline-blue" href="#">Read More <svg viewBox="0 0 14 8"><path d="M0 4h12M9 1l3 3-3 3" stroke="currentColor" fill="none"/></svg></a>
</section>

<section class="cloud abs">
  <div class="city abs" role="img" aria-label="Illustration of a city skyline with buildings, people and a bus connected by network lines"></div>
  <div class="city-band abs"></div>
  <div class="c1 abs">
    <h3>CLOUD COMPUTING</h3>
    <p>There are many variations of passages of Lorem Ipsum available, but the majority have suffered alteration in some form, by injected humour, or randomised words which don't look even slightly believable.</p>
    <a class="btn btn-dark" href="#">Read More <svg viewBox="0 0 14 8"><path d="M0 4h12M9 1l3 3-3 3" stroke="currentColor" fill="none"/></svg></a>
  </div>
  <div class="c2 abs">
    <h3>DATACENTER SOLUTIONS</h3>
    <p>There are many variations of passages of Lorem Ipsum available, but the majority have suffered alteration in some form, by injected humour, or randomised words which don't look even slightly believable.</p>
    <a class="btn btn-dark" href="#">Read More <svg viewBox="0 0 14 8"><path d="M0 4h12M9 1l3 3-3 3" stroke="currentColor" fill="none"/></svg></a>
  </div>
</section>

<section class="server abs" role="img" aria-label="Photo of a dark server room aisle with racks">
  <h2>SERVER INFRASTRUCTURE / <span>NETWORKING</span></h2>
  <p>There are many variations of passages of Lorem Ipsum available, but the majority have suffered alteration in some form, by injected humour,</p>
  <a class="btn btn-ghost" href="#">Read More <svg viewBox="0 0 14 8"><path d="M0 4h12M9 1l3 3-3 3" stroke="currentColor" fill="none"/></svg></a>
</section>

<section class="project abs">
  <div class="team-photo abs" role="img" aria-label="Photo of two colleagues reviewing a plan on a clipboard"></div>
  <h2 class="abs">PROJECT MANAGEMENT</h2>
  <p class="intro abs">There are many variations of passages of Lorem Ipsum available, but the majority have suffered alteration in some form, by injected humour, or randomised words which don't look even slightly believable.</p>
  <h3 class="abs">Lorem Ipsum available</h3>
  <ul class="list-a abs">
    <li>Lorem Ipsum available</li><li>Lorem Ipsum available</li><li>Lorem Ipsum available</li><li>Lorem Ipsum available</li><li>Lorem Ipsum available</li>
  </ul>
  <ul class="list-b abs">
    <li>Lorem Ipsum available</li><li>Lorem Ipsum available</li><li>Lorem Ipsum available</li>
  </ul>
  <a class="btn btn-red" href="#">Read More <svg viewBox="0 0 14 8"><path d="M0 4h12M9 1l3 3-3 3" stroke="currentColor" fill="none"/></svg></a>
</section>

<a class="btn btn-red remote" href="#">Remote Support <svg viewBox="0 0 14 8" style="width:8px"><path d="M2 2l5 4 5-4" stroke="currentColor" fill="none"/></svg></a>

<footer class="site-footer abs">
  <p class="copyright abs">© 2015 larkspur systems group . All rights reserved.</p>
  <div class="footer-brand abs">
    <span class="brand-mark"></span>
    <span class="brand-name">Larkspur Systems Group</span>
  </div>
  <nav class="social abs" aria-label="Social media">
    <a href="#" style="background:#3b5998" aria-label="Social link 1"></a>
    <a href="#" style="background:#cb2027" aria-label="Social link 2"></a>
    <a href="#" style="background:#2ba9e1" aria-label="Social link 3"></a>
    <a href="#" style="background:#355c8c" aria-label="Social link 4"></a>
    <a href="#" style="background:#6a4a3c" aria-label="Social link 5"></a>
  </nav>
</footer>

</body>
</html>
```